Buch-/E-Book-Cover für History-Thriller Die Glasbläserin
Ich habe ein ebook-cover für einen History-Thriller gesucht. Bereits der erste Entwurf der Designerin Lorabe hat mich grundsätzlich voll überzeugt. Es waren nur noch Details zu verändern. Es wurde jederzeit sehr schnell auf meine Kommentare reagiert und meine Wünsche darin zur vollsten Zufriedenheit umgesetzt. Ich bin auf ganzer Linie mit dem Gewinnerdesign und der Arbeitsweise der Designerin Lorabe zufrieden und empfehle sie zu 100% weiter! Vielen Dank für die tolle Arbeit
Zielgruppe
Autor im Spannungsbereich / Anspruchsvolle Leser/innen
Aufgabenstellung
Buchcover für einen historischen Thriller aus der Zeit des Zweiten Weltkriegs gesucht.
Titel: Die Glasbläserin (unten, groß, gut lesbar)
Autor: Jonas Wendel (oben, etwas kleiner)
Hintergrund: leicht sepiafarben, Schriftarten sollten dazu passen.
Rechts im Vordergrund sollte eine attraktive, aber entschlossen blickende Frau in den Dreißigern mit dunklen Locken und zeitgenössischer Kleidung zu sehen sein. Ideal wäre z.B. Trenchcoat, mittellanger Rock, schwarze Strumpfhosen. Evtl. auch Hut. Sie dreht sich seitlich zum Betrachter um. In der linken, nach unten hängenden Hand wäre eine Pistole wünschenswert (typische Agentenwaffe "Brenner KX7"). Alternative wäre eine Aktentasche möglich.
Die Perspektive zeigt eine Straße, evtl. Kopfsteinpflaster, die auf eine historische Fassade zuläuft (schön wäre das "Graf-Albrecht-Akademie", vgl. anl. Datei)
Da rechts der Kopf der Protagonistin zu sehen sein soll, wäre die Fassade bevorzugt im linken oberen Drittel des Covers anzubringen.
Nur zwecks stilistischer bzw. farblicher Orientierung sei auf "Die Füchsin" von Tom Barrow oder auch (weniger) auf "Aschenmond" von Gerda Pfalzl verwiesen.
Für die Rückseite des Buchumschlags/Klappentext wird ein einfacher Hintergrund benötigt, der die Hintergrundfarben der Vorderseite ohne Motiv wiedergibt.

```html
<!DOCTYPE html>
<html lang="de">
<head>
<meta charset="utf-8">
<title>Die Glasbläserin – Umschlag</title>
<link rel="stylesheet" href="https://fonts.googleapis.com/css2?family=Bebas+Neue&family=Dosis:wght@300;400&display=swap">
<style>
  :root {
    --stage: #eceef0;
    --paper-light: #fbf0dc;
    --paper-mid: #f3e2c2;
    --paper-edge: #e9d3ab;
    --ink: #2a2622;
    --title-red: #a82a3e;
    --frame: #9a958e;
  }
  * { margin: 0; padding: 0; box-sizing: border-box; }
  html, body {
    width: 938px; height: 1200px; overflow: hidden;
    background: var(--stage);
  }
  .stage {
    position: relative; width: 938px; height: 1200px;
  }
  .wrap {
    position: absolute; left: 48px; top: 315px;
    width: 842px; height: 570px;
    border: 1px solid var(--frame);
    background:
      radial-gradient(ellipse at 30% 20%, var(--paper-light) 0%, transparent 60%),
      radial-gradient(ellipse at 80% 10%, var(--paper-edge) 0%, transparent 45%),
      linear-gradient(180deg, var(--paper-mid) 0%, var(--paper-light) 55%, var(--paper-mid) 100%);
    overflow: hidden;
  }
  .back-blurb {
    position: absolute; left: 64px; top: 93px; width: 270px;
    font-family: "Dosis", sans-serif; font-weight: 300;
    font-size: 10.2px; line-height: 16.6px; color: var(--ink);
  }
  .back-blurb p + p { margin-top: 16.6px; }
  .scene {
    position: absolute; left: 380px; top: 150px;
    width: 462px; height: 420px;
  }
  .spine-title, .spine-author {
    position: absolute; left: 420px;
    transform: translateX(-50%) rotate(90deg);
    white-space: nowrap; transform-origin: center;
  }
  .spine-title {
    top: 187px;
    font-family: "Bebas Neue", sans-serif; font-size: 19px;
    letter-spacing: 0.5px; color: var(--title-red);
  }
  .spine-author {
    top: 405px;
    font-family: "Dosis", sans-serif; font-weight: 400;
    font-size: 11px; color: var(--ink);
  }
  .front-author {
    position: absolute; left: 484px; width: 312px; top: 48px;
    text-align: center;
    font-family: "Dosis", sans-serif; font-weight: 400;
    font-size: 21.5px; color: var(--ink);
  }
  .front-title {
    position: absolute; left: 470px; width: 340px; top: 84px;
    text-align: center;
    font-family: "Bebas Neue", sans-serif; font-size: 60px;
    line-height: 62px; letter-spacing: 1px; color: var(--title-red);
  }
  .front-genre {
    position: absolute; left: 484px; width: 312px; top: 525px;
    text-align: center;
    font-family: "Dosis", sans-serif; font-weight: 400;
    font-size: 19px; color: var(--ink);
  }
</style>
</head>
<body>
<main class="stage">
  <section class="wrap">
    <div class="back-blurb">
      <p>Rückklappentext: Soloria culpa volum quam illate volore­henit utendic tempel ium natur molenimus aut aliquuntios maio berum, corem quodips untinci dolest, sant dis de verupta dolor rem. Musanie nisquossum ut as sequae num estruptur? Qui sitium es alit omnim fugias dolecum nis maximus dandelia sunti rae eicit ut venet, aut aut audia sin nonet, apellibus, ullore consequ atinven impelic ipictas quibers piduntent inis</p>
      <p>Tem ut ea soluptate eic tem aut as dollabore sin et vo­luptaquo eoste pore volorit erate sequis ullore culpa quos dolupta nimus net aut pel molupta sequas doluptatem rese non cum que commolu ptatem quam inversp er­ehend ipsusanda sa que et el in etur? Incipiet et, eserum andaeperiate natqui acepro volorum dellectes et harum nos as est post, quo magnate ommolorepudi omnim haruptatent as earchicae sam sitibus, undandi te voluptat magnime ndandic totatiur sapis perciendae.</p>
      <p>Ebit alignis saeruptat ipid ut aditatur. Aped qui as mintemp oribus dolorestiae nihicaeculla dolupta tiunto cum entis isincip saeperume volor min repudae eaquis adi siminctora voluptat omni is sitia si quo tem corporem.</p>
    </div>

    <svg class="scene" viewBox="0 0 462 420" role="img"
         aria-label="Sepiafoto: Frau in gelber Jacke und rotbraunem Faltenrock von hinten, auf einem Kopfsteinpflasterplatz vor historischen Fassaden">
      <defs>
        <linearGradient id="sceneTone" x1="0" y1="0" x2="0" y2="1">
          <stop offset="0" stop-color="#f3e2c2" stop-opacity="0"/>
          <stop offset="0.35" stop-color="#cfc8bb" stop-opacity="0.55"/>
          <stop offset="0.55" stop-color="#b9b2a6" stop-opacity="0.6"/>
          <stop offset="0.7" stop-color="#e6d6ba" stop-opacity="0.6"/>
          <stop offset="1" stop-color="#e2cfae" stop-opacity="0.5"/>
        </linearGradient>
        <linearGradient id="sceneFade" x1="0" y1="0" x2="1" y2="0">
          <stop offset="0" stop-color="#fff" stop-opacity="0"/>
          <stop offset="0.12" stop-color="#fff" stop-opacity="1"/>
          <stop offset="1" stop-color="#fff" stop-opacity="1"/>
        </linearGradient>
        <mask id="sceneMask"><rect width="462" height="420" fill="url(#sceneFade)"/></mask>
        <linearGradient id="figureTone" x1="0" y1="0" x2="0" y2="1">
          <stop offset="0" stop-color="#6f6a74" stop-opacity="0.5"/>
          <stop offset="0.3" stop-color="#d9c46e" stop-opacity="0.55"/>
          <stop offset="0.5" stop-color="#8a4a40" stop-opacity="0.55"/>
          <stop offset="0.8" stop-color="#8a4a40" stop-opacity="0.45"/>
          <stop offset="1" stop-color="#e2cfae" stop-opacity="0"/>
        </linearGradient>
      </defs>
      <rect width="462" height="420" fill="url(#sceneTone)" mask="url(#sceneMask)"/>
      <rect x="225" y="55" width="110" height="300" rx="40" fill="url(#figureTone)"/>
    </svg>

    <div class="spine-title">Die Glasbläserin</div>
    <div class="spine-author">Jonas Wendel</div>

    <div class="front-author">Jonas Wendel</div>
    <h1 class="front-title">Die Glasbläserin</h1>
    <div class="front-genre">THRILLER</div>
  </section>
</main>
</body>
</html>
```